Business Card Design

VEGETABLE FARMING OPERATION PRIMARY CROPS SPINACH,SPRING MIX, HEAD LETTUCE, ROMAINE, BRUSSEL SPROUTS, KESTREL STEM GREENS BROCCOLI CAULIFLOWER CELERY NEED A Business card THAT REPRESENTS SOME OF THOSE CROPS AY IDEAS WELCOME..

The business is vegetable farming spinach spring mix head lettuce romaine broccoli brussel sprouts celery carrots target audience is potential shippers of products week spring mix spinach harvesting as well. I colors in mind just need a card that's original

Industry/Entity Type

Farming

Contact Information for Business Card

R&T FARMS LLC WILLOWDALE FARMS LLC

```html
<!DOCTYPE html>
<html lang="en">
<head>
<meta charset="utf-8">
<title>R&amp;T Farms – Business Card</title>
<link rel="stylesheet" href="https://fonts.googleapis.com/css2?family=Roboto+Condensed:wght@700&display=swap">
<style>
  :root {
    --backdrop-deep: #0a1a1b;
    --backdrop-mid: #12302f;
    --backdrop-vein: #1d4644;
    --card-white: #ffffff;
    --lime: #8cff14;
    --text-white: #ffffff;
    --text-shade: rgba(24, 78, 6, 0.75);
    --veg-light: #d9f2b8;
    --veg-mid: #9fdc5a;
    --veg-dark: #5aa829;
  }
  html, body {
    margin: 0;
    padding: 0;
    width: 1200px;
    height: 877px;
    overflow: hidden;
    background: var(--backdrop-deep);
  }
  .canvas {
    position: relative;
    width: 1200px;
    height: 877px;
    background:
      radial-gradient(ellipse 320px 180px at 180px 140px, var(--backdrop-vein), transparent 70%),
      radial-gradient(ellipse 260px 220px at 1020px 240px, var(--backdrop-vein), transparent 70%),
      radial-gradient(ellipse 380px 200px at 640px 90px, var(--backdrop-mid), transparent 70%),
      radial-gradient(ellipse 300px 240px at 150px 620px, var(--backdrop-mid), transparent 70%),
      radial-gradient(ellipse 340px 200px at 1050px 700px, var(--backdrop-vein), transparent 70%),
      radial-gradient(ellipse 420px 160px at 600px 780px, var(--backdrop-mid), transparent 70%),
      linear-gradient(135deg, #0d2324 0%, #0a1819 45%, #10292a 100%);
  }
  .business-card {
    position: absolute;
    left: 228px;
    top: 258px;
    width: 660px;
    height: 352px;
    border-radius: 18px;
    overflow: hidden;
    display: flex;
    font-family: "Roboto Condensed", "Arial Narrow", sans-serif;
  }
  .card-art-side {
    position: relative;
    width: 329px;
    height: 100%;
    background: var(--card-white);
  }
  .rule {
    position: absolute;
    height: 5px;
    background: var(--lime);
  }
  .rule-top { left: 26px; top: 67px; width: 262px; }
  .rule-bottom { left: 30px; top: 273px; width: 262px; }
  .vegetable-art {
    position: absolute;
    left: 64px;
    top: 94px;
    width: 214px;
    height: 146px;
  }
  .card-info-side {
    flex: 1;
    background: var(--lime);
    position: relative;
  }
  .company-names {
    margin: 0;
    color: var(--text-white);
    font-weight: 700;
    line-height: 1;
    text-shadow: 0 1px 2px var(--text-shade), 0 0 1px var(--text-shade);
  }
  .company-names span {
    position: absolute;
    left: 0;
    right: 0;
    text-align: center;
    white-space: nowrap;
  }
  .company-name {
    font-size: 21px;
    letter-spacing: 2.2px;
    padding-left: 2.2px;
  }
  .company-name-first { top: 120px; }
  .company-name-second { top: 156px; }
  .operation-type {
    top: 193px;
    font-size: 17px;
    letter-spacing: 2.4px;
    padding-left: 2.4px;
  }
</style>
</head>
<body>
<div class="canvas">
  <section class="business-card">
    <div class="card-art-side">
      <div class="rule rule-top"></div>
      <svg class="vegetable-art" role="img" aria-label="Illustration of cauliflower, broccoli, celery and cabbage" viewBox="0 0 214 146">
        <defs>
          <linearGradient id="vegTones" x1="0" y1="0" x2="1" y2="1">
            <stop offset="0" stop-color="#d9f2b8"/>
            <stop offset="0.55" stop-color="#9fdc5a"/>
            <stop offset="1" stop-color="#5aa829"/>
          </linearGradient>
        </defs>
        <rect x="0" y="0" width="214" height="146" rx="10" fill="url(#vegTones)"/>
      </svg>
      <div class="rule rule-bottom"></div>
    </div>
    <div class="card-info-side">
      <p class="company-names">
        <span class="company-name company-name-first">R&amp;T FARMS LLC</span>
        <span class="company-name company-name-second">WILLOWDALE FARMS LLC</span>
        <span class="operation-type">(VEGETABLE FARMING OPERATION)</span>
      </p>
    </div>
  </section>
</div>
</body>
</html>
```